Semi Permanent make up flyer

Hi

I will be sending a few thousand flyers dropped door to door in some very lovely parts of London.

The flyer must contain the following information;

New studio in Greenwich

Velmira Lineo trained technician - gold advanced level

Free consultation no obligation

Price List;
Eyebrow hair stroke: £325
Eyebrows 3D effect: £395
Microblading hair stroke: £330
Eyelash enhancement Top: £250
Eyelash enhancement Top & Bottom: £300
Lip blush: £450

Tel;……………….
Facebook: Odelie Permanent Cosmetics
Instagram: Odelie_Permanent_Cosmetics

Special introductory offers - available for a limited time only;
Like & share my page for 10% off any treatment
Refer a friend for £50 off each
Buy one treatment get 50% off another

I would like it to look clean, professional, expensive, and high end/luxury

I’m happy to make this a double sided print so I can have my logo on the front and the information on the back.

It must include my logo.

If you could use images of appealing women I think it would work best. Images have to have nice eyes, lips and brows. Weather you use entire face or features that is up to you.

Please show me a selection of different colour ways across the whole design. I personally feel softer tones would work. No black or bright colours.

I will be getting my new phone number in the next few days. I will let you know via messages what it is for you to add it in.

Any questions feel free to ask.

Target Market(s)

Women

Industry/Entity Type

Beauty Salon

Font styles to use
Sans Serif

Requirements
Must have
• Everything in Description
Nice to have
• The designers give their ideas. Im looking for input
Should not have
• Childish, cheap images or fonts. This is very high end so needs to look it

```html
<!DOCTYPE html>
<html lang="en">
<head>
<meta charset="utf-8">
<title>Odelie Permanent Cosmetics – Flyer</title>
<link rel="stylesheet" href="https://fonts.googleapis.com/css2?family=Raleway:wght@300;400;600&display=swap">
<style>
  :root {
    --page: #ffffff;
    --peach: #fdeadb;
    --peach-light: #fdf1e8;
    --strip: #fcf3ed;
    --ink: #5a5450;
    --ink-soft: #6e6762;
    --gold: #c9a04a;
    --skin-a: #f6dccb;
    --skin-b: #eec7b1;
    --hair: #3b2f2a;
  }
  * { margin: 0; padding: 0; box-sizing: border-box; }
  html, body { width: 1200px; height: 900px; overflow: hidden; background: var(--page); }
  body { font-family: "Raleway", sans-serif; color: var(--ink); position: relative; }

  .panel { position: absolute; top: 15px; height: 825px; }
  .front { left: 17px; width: 578px; background: var(--peach); }
  .back-strip { left: 607px; width: 188px; background: var(--strip); box-shadow: 4px 0 8px rgba(120,90,70,.18); z-index: 2; }
  .back-main { left: 795px; width: 388px; background: var(--peach-light); overflow: hidden; }

  .portrait {
    position: absolute; left: 368px; top: 0; width: 210px; height: 825px;
    background: linear-gradient(180deg, var(--hair) 0%, #5a463c 22%, var(--skin-a) 30%, var(--skin-b) 60%, var(--skin-a) 85%, var(--peach) 100%);
  }
  .portrait-faint {
    position: absolute; left: 0; top: 0; width: 220px; height: 100%;
    background: linear-gradient(180deg, rgba(150,130,120,.18) 0%, rgba(238,199,177,.28) 40%, rgba(253,241,232,0) 100%);
  }

  .tagline { position: absolute; left: 0; width: 355px; top: 38px; text-align: center; font-weight: 300; font-size: 22px; line-height: 29.5px; letter-spacing: .5px; }
  .tagline .accent { color: var(--gold); }
  .location { position: absolute; left: 0; width: 355px; top: 288px; text-align: center; font-weight: 300; font-size: 17px; letter-spacing: .3px; }

  .brand-front { position: absolute; left: 0; width: 355px; top: 560px; text-align: center; color: var(--ink); font-weight: 300; }
  .brand-front .name { display: block; font-size: 34px; letter-spacing: 18px; padding-left: 18px; }
  .brand-front .sub { display: block; font-size: 17px; letter-spacing: 3.5px; margin-top: 8px; }

  .social { position: absolute; display: flex; align-items: center; gap: 10px; font-size: 11px; font-weight: 400; color: var(--ink-soft); }
  .social .dot { width: 22px; height: 22px; background: var(--ink); border-radius: 3px; flex: none; }
  .social .dot.round { border-radius: 50%; }

  .brand-strip { position: absolute; left: 0; width: 188px; top: 110px; text-align: center; color: var(--ink); font-weight: 300; }
  .brand-strip .name { display: block; font-size: 13px; letter-spacing: 6px; padding-left: 6px; }
  .brand-strip .sub { display: block; font-size: 6.5px; letter-spacing: 1.2px; margin-top: 3px; }

  .offers { position: absolute; left: 0; width: 188px; top: 190px; text-align: center; }
  .offers h2 { font-weight: 600; font-size: 19px; line-height: 28px; letter-spacing: 1px; color: var(--ink); margin-bottom: 30px; }
  .offer { font-size: 13px; font-weight: 400; line-height: 17px; margin-bottom: 24px; color: var(--ink-soft); }
  .offer strong { display: block; font-size: 17px; font-weight: 600; color: var(--ink); line-height: 22px; }
  .limited { position: absolute; left: 0; width: 188px; top: 643px; text-align: center; font-size: 8px; letter-spacing: .3px; color: var(--ink-soft); }

  .consult { position: absolute; left: 0; width: 388px; top: 50px; text-align: center; font-weight: 300; font-size: 24px; line-height: 34px; }
  .prices { position: absolute; left: 0; width: 388px; top: 160px; list-style: none; text-align: center; }
  .prices li { height: 71.5px; }
  .prices .item { display: block; font-size: 13px; font-weight: 400; letter-spacing: .2px; color: var(--ink-soft); }
  .prices .cost { display: block; font-size: 18px; font-weight: 300; margin-top: 4px; }
  .credential { position: absolute; left: 0; width: 388px; top: 603px; text-align: center; }
  .credential .trained { font-size: 13px; font-weight: 400; color: var(--ink-soft); }
  .credential .level { font-size: 21px; font-weight: 300; color: var(--gold); margin-top: 6px; letter-spacing: .5px; }
  .call { position: absolute; left: 0; width: 388px; top: 690px; text-align: center; font-weight: 300; }
  .call .label { font-size: 19px; }
  .call .number { font-size: 36px; letter-spacing: 1px; }
</style>
</head>
<body>

<section class="panel front">
  <div class="portrait" role="img" aria-label="Close-up photograph of a woman with sleek dark hair, closed eye with soft blue eyeshadow and coral lips"></div>
  <p class="tagline">WHEN<br>THE<br>APPEAL<br>FOR<br><span class="accent">BEAUTY</span><br>MATTERS</p>
  <p class="location">NEW STUDIO IN GREENWICH</p>
  <p class="brand-front"><span class="name">ODELIE</span><span class="sub">PERMANENT COSMETICS</span></p>
  <div class="social" style="left:206px; top:782px;"><span class="dot"></span>Odelie Permanent Cosmetics</div>
  <div class="social" style="left:396px; top:782px;"><span class="dot round"></span>Odelie Permanent Cosmetics</div>
</section>

<section class="panel back-strip">
  <p class="brand-strip"><span class="name">ODELIE</span><span class="sub">PERMANENT COSMETICS</span></p>
  <div class="offers">
    <h2>SPECIAL<br>INTRODUCTORY<br>OFFERS</h2>
    <p class="offer">LIKE &amp; SHARE<br>MY PAGE<br>FOR<strong>10% OFF</strong>ANY TREATMENT</p>
    <p class="offer">REFER A FRIEND<br>FOR<strong>£50 OFF</strong>EACH</p>
    <p class="offer">BUY ONE TREATMENT<br>&amp; GET<strong>50% OFF</strong>ANOTHER</p>
  </div>
  <p class="limited">AVAILABLE FOR A LIMITED TIME ONLY</p>
  <div class="social" style="left:13px; top:676px; font-size:10px;"><span class="dot"></span>Odelie Permanent Cosmetics</div>
  <div class="social" style="left:13px; top:720px; font-size:10px;"><span class="dot round"></span>Odelie Permanent Cosmetics</div>
</section>

<section class="panel back-main">
  <div class="portrait-faint" role="img" aria-label="Faint background photograph of a woman's face with closed eyes"></div>
  <p class="consult">FREE CONSULTATION<br>NO OBLIGATION</p>
  <ul class="prices">
    <li><span class="item">EYEBROW HAIR STROKE</span><span class="cost">£325</span></li>
    <li><span class="item">EYEBROWS 3D EFFECT</span><span class="cost">£395</span></li>
    <li><span class="item">MICROBLADING HAIR STROKE</span><span class="cost">£330</span></li>
    <li><span class="item">EYELASH ENHANCEMENT TOP</span><span class="cost">£250</span></li>
    <li><span class="item">EYELASH ENHANCEMENT TOP &amp; BOTTOM</span><span class="cost">£300</span></li>
    <li><span class="item">LIP BLUSH</span><span class="cost">£450</span></li>
  </ul>
  <div class="credential">
    <p class="trained">VELMIRA LINEO TRAINED TECHNICIAN</p>
    <p class="level">GOLD ADVANCED LEVEL</p>
  </div>
  <div class="call">
    <p class="label">CALL US</p>
    <p class="number">000 0000 000</p>
  </div>
</section>

</body>
</html>
```